Banner Ad Design Project

we are a tax resolution (help with the QRA)/accounting firm that has begun a radio campaign in south florida (am 640 and am 850). we need a banner ad, 250 x 300, that will run on the stations websites. We have a logo that can be used, check it out on our website, www.marlowfiscalaid.com. Also, we have zentrix banner ads that are running on 850 am already:

https://promo.zentrixads.example/da/b/preview?ad=1234567890&adGroup=1098765432&destinationUrl=http://book.marlowfiscalaid.com/reserve-a-session-with-a-fiscal-advisor/&height=250&hl=en_US&key=-1111222233334444555&isExpandable=false&ocid=1212343456&outputFormat=FLASH&s=61&templateId=117&visibleUrl=WWW.MARLOWFISCALAID.COM&width=300&sig=QWeRtYuIoP12-asdfGHJKLzxcvbnm0987

https://promo.zentrixads.example/da/b/preview?ad=1234567111&adGroup=1098765432&destinationUrl=http://book.marlowfiscalaid.com/reserve-a-session-with-a-fiscal-advisor/&height=250&hl=en_US&key=-6666777788889999000&isExpandable=false&ocid=1212343456&outputFormat=FLASH&s=61&templateId=24&visibleUrl=www.marlowfiscalaid.com&width=300&sig=ZxCvBnMaSd34-qwertyPLMOKNijbuhv765

we need something different and creative that will drive traffic to our site.

Thanks

```html
<!DOCTYPE html>
<html lang="en">
<head>
<meta charset="utf-8">
<title>QRA Problems Banner</title>
<link rel="stylesheet" href="https://fonts.googleapis.com/css2?family=PT+Sans+Narrow:wght@400;700&family=PT+Sans:ital,wght@0,400;0,700;1,400&display=swap">
<style>
  :root {
    --page: #ffffff;
    --banner-red: #c1302e;
    --banner-edge: #d9d9d9;
    --ink: #111111;
    --shadow: #2a2a2a;
    --footer-bar: #050505;
    --brand-navy: #2c2f7a;
    --button-navy: #2b2f6b;
    --button-edge: #c9cbe0;
    --badge-blue: #2d5f9a;
    --white: #ffffff;
  }
  html, body {
    margin: 0;
    padding: 0;
    width: 1200px;
    height: 800px;
    overflow: hidden;
    background: var(--page);
  }
  .canvas {
    position: relative;
    width: 1200px;
    height: 800px;
  }
  .ad {
    position: absolute;
    left: 280px;
    top: 262px;
    width: 600px;
    height: 354px;
    background: var(--white);
    box-shadow: 6px 6px 8px rgba(0,0,0,0.55);
  }
  .headline-band {
    position: absolute;
    left: -6px;
    top: -8px;
    width: 604px;
    height: 94px;
    background: var(--banner-red);
    border: 4px solid var(--banner-edge);
    box-shadow: 5px 6px 0 var(--shadow);
    display: flex;
    align-items: center;
    justify-content: center;
  }
  .headline {
    margin: 0;
    font-family: "PT Sans Narrow", sans-serif;
    font-weight: 400;
    font-size: 82px;
    letter-spacing: 1px;
    color: var(--white);
    line-height: 1;
    text-shadow: 2px 2px 2px rgba(0,0,0,0.35);
  }
  .message {
    position: absolute;
    top: 106px;
    left: 0;
    width: 600px;
    text-align: center;
    font-family: "PT Sans", sans-serif;
    font-style: italic;
    color: var(--ink);
  }
  .message p { margin: 0; }
  .message .lead { font-size: 25px; line-height: 32px; }
  .message .claim { font-size: 25px; line-height: 32px; }
  .message .proof { font-size: 21px; line-height: 30px; }
  .brand {
    position: absolute;
    left: 16px;
    top: 256px;
    display: flex;
    align-items: center;
    gap: 10px;
  }
  .brand-mark {
    width: 22px;
    height: 22px;
    background: var(--brand-navy);
  }
  .brand-name {
    font-family: "PT Sans", sans-serif;
    font-weight: 700;
    font-size: 26px;
    color: var(--brand-navy);
  }
  .accreditation {
    position: absolute;
    left: 316px;
    top: 250px;
    width: 22px;
    height: 30px;
    background: var(--badge-blue);
    border-radius: 3px;
  }
  .cta {
    position: absolute;
    left: 396px;
    top: 268px;
    width: 158px;
    height: 38px;
    background: var(--button-navy);
    border: 3px solid var(--button-edge);
    outline: 2px solid var(--button-navy);
    border-radius: 5px;
    color: var(--white);
    font-family: "PT Sans", sans-serif;
    font-size: 23px;
    line-height: 38px;
    text-align: center;
    letter-spacing: 0.5px;
  }
  .footer-bar {
    position: absolute;
    left: 0;
    bottom: 0;
    width: 600px;
    height: 24px;
    background: var(--footer-bar);
  }
</style>
</head>
<body>
<div class="canvas">
  <div class="ad">
    <div class="headline-band">
      <h1 class="headline">QRA PROBLEMS ?</h1>
    </div>
    <div class="message">
      <p class="lead">Don’t Wait.</p>
      <p class="claim">Let Us Help Solve Your QRA Issues Today.</p>
      <p class="proof">We’ve successfully helped thousands of clients, just like you</p>
      <p class="proof">with Tax Levis, Garnishments, Liens and more!</p>
    </div>
    <div class="brand">
      <span class="brand-mark"></span>
      <span class="brand-name">Marlow &amp; Partners, Inc.</span>
    </div>
    <div class="accreditation" aria-hidden="true"></div>
    <div class="cta">LEARN MORE</div>
    <div class="footer-bar"></div>
  </div>
</div>
</body>
</html>
```